Veteran owned/staffed Organization that hires Veterans into Ironworking

Please see attached documents for all details and info.
We want a tri-fold brochure to use as a recruiting tool.
Our slogan is:
"Revolutionizing the skilled workforce, one Veteran at a time"
Veteran Apprenticeship Program in Ironworking
Skills/Traits: Welding, bolting, rigging, connecting
Teamwork, camaraderie, TK Grant, Skilled Labor, Career, Community service
OJT, Apprenticeship, Career
Due to the large number of retirees from the baby boomer generation, ironworkers are in high demand. In Texas, the construction industry is on the rise and due to our training regiment, an average of 40 hrs/wk are worked. Our apprenticeship program follows the PLWTO curriculum and at the end of the 3-year course involving classroom learning, OJT and practical application the apprentice achieves journeymen status in ironworking. Journeyman status opens the door to possible postions like foremen, crane operators and project managers. Ironworkers perform their duties on steel structures that provide a skeleton for commercial buildings like hospitals, schools and skyscrapers. Some of the key skilled trades of ironworking are welding, rigging, bolting and connecting.
All Things Veterans
Camaraderie and Culture
-Veteran owned and majority staffed organization who are committed to the mission of providing opportunitites to Veterans
-Graduation celebration after completion of initial training period, holiday parties and get togethers at HQBs
-Work with other Veterans and always have your teammate’s six
-We’re building America, one Veteran career at a time
Professional Support
BDR is committed to providing Veterans with supportive services designed to assist you and your families in the following areas:
Financial, family and work-related support.
Community Service
Disaster Response
Louisiana Flooding - Sept 2016
As the 15th anniversery of 9/11 approached BDR worked to find a volunteer opportunity. An ambitious plan was formed to respond to the devastating 1000-year flood event in Baton Rouge. With little time for planning, BDR organized all the tools and supplies necessary to take 24 Veterans to assist a community in extreme poverty. The team gutted the homes of nine residents which included: single mothers, handicapped elderaly and a Korean War Veterans
Hurricane Orlend - Oct 2016
In a period of 24 hours BDR mobilized 16 Veterans with the supplies neccessary to be 100% self-reliant. The team arrived in Holly Hill, SC 8 hours after Hurrican Orlend made landfall. During a period of 2 days, BDR provided over 5,000 meals, distributed 40,000 bottles of water and removed nearly 100 trees.

Target Market(s)

Veterans who are interested in becoming Ironworkers. Usually under the age of 40, have served in the military and are in the Texas area.

Industry/Entity Type

Construction

Font styles to use
Other font styles liked:
• Microgramma in some places (Logo font) and Serif type font for the bulk

Requirements
Must have
• The colors and logo mentioned in the template guidelines document.
• The slogan
• "Revolutionizing the skilled workforce, one Veteran at a time"
Nice to have
• Some charts and graphs if possible?

```html
<!DOCTYPE html>
<html lang="en">
<head>
<meta charset="utf-8">
<title>BDR Tri-fold Brochure</title>
<link href="https://fonts.googleapis.com/css2?family=Montserrat:wght@400;600;800&family=Lato:wght@400;700&display=swap" rel="stylesheet">
<style>
  :root {
    --navy: #1c2a45;
    --navy-deep: #142036;
    --gold: #e9b15c;
    --gold-dark: #b8843a;
    --white: #ffffff;
    --page: #f1f1f1;
    --sky: #a9c8e6;
    --steel: #6b5a55;
  }
  * { box-sizing: border-box; margin: 0; padding: 0; }
  html, body { width: 1200px; height: 898px; overflow: hidden; background: var(--page); }
  .brochure { position: relative; width: 1200px; height: 898px; }
  .panel {
    position: absolute; top: 19px; width: 384px; height: 860px;
    background: var(--navy); overflow: hidden; color: var(--white);
    font-family: "Lato", sans-serif;
  }
  .panel--inside { left: 24px; }
  .panel--back { left: 408px; }
  .panel--cover { left: 792px; }
  .panel svg.shapes { position: absolute; inset: 0; width: 384px; height: 860px; }

  /* inside panel */
  .skills { position: absolute; top: 40px; left: 30px; right: 30px; }
  .section-title {
    font-family: "Montserrat", sans-serif; font-weight: 800; color: var(--gold);
    font-size: 17px; letter-spacing: .5px;
  }
  .skills .section-title { text-align: center; margin-bottom: 10px; }
  .skill-columns { display: flex; justify-content: space-between; padding: 0 18px; }
  .skill-list { list-style: none; font-size: 12.5px; line-height: 1.35; }
  .skill-list li::before { content: "•"; color: var(--gold); margin-right: 7px; }
  .career { position: absolute; top: 168px; left: 30px; right: 30px; }
  .career .section-title { margin-bottom: 8px; }
  .career p { font-size: 11.6px; line-height: 1.5; text-align: justify; }

  /* back panel */
  .logo { position: absolute; left: 0; right: 0; text-align: center; }
  .logo__mark {
    display: inline-flex; align-items: center; gap: 10px;
    font-family: "Montserrat", sans-serif; font-weight: 800; color: var(--gold);
    font-size: 40px; letter-spacing: 3px;
  }
  .logo__dot { width: 14px; height: 14px; border-radius: 50%; background: var(--gold); display: inline-block; }
  .logo__name {
    display: block; margin-top: 4px; font-family: "Montserrat", sans-serif; font-weight: 600;
    color: var(--gold); font-size: 10px; letter-spacing: 1.5px;
  }
  .panel--back .logo { top: 292px; }
  .photo-frames { position: absolute; top: 420px; left: 34px; display: flex; gap: 22px; }
  .photo-frame {
    width: 147px; height: 104px; border: 4px solid var(--gold); border-radius: 14px;
    background: linear-gradient(160deg, #8fb6df, #3f5778 70%, #2b3a52);
  }
  .photo-frame--beam { background: linear-gradient(150deg, #c9dcef, #7ea3cc 60%, #4e3e3a); }
  .contact { position: absolute; top: 585px; left: 0; right: 0; text-align: center; }
  .contact__phone { font-size: 19px; font-weight: 700; letter-spacing: .3px; }
  .contact__email { margin-top: 8px; font-size: 14px; color: var(--gold); font-weight: 700; }
  .contact__web { margin-top: 10px; font-size: 15px; letter-spacing: 6px; }

  /* cover panel */
  .panel--cover .logo { top: 70px; }
  .slogan { position: absolute; top: 640px; left: 0; right: 0; text-align: center; font-family: "Montserrat", sans-serif; }
  .slogan__lead { font-size: 24px; font-weight: 400; letter-spacing: 1px; }
  .slogan__main { font-size: 26px; font-weight: 800; margin-top: 2px; }
  .slogan__tail { font-size: 23px; font-weight: 400; margin-top: 2px; letter-spacing: .5px; }
  .web-pill {
    position: absolute; top: 768px; left: 50%; transform: translateX(-50%);
    width: 290px; height: 44px; border: 2px solid var(--gold); border-radius: 22px;
    display: flex; align-items: center; justify-content: center;
    font-size: 15px; letter-spacing: 7px; color: var(--white);
  }
</style>
</head>
<body>
<main class="brochure">

  <!-- Inside panel: skills and career text -->
  <section class="panel panel--inside">
    <svg class="shapes" viewBox="0 0 384 860" aria-hidden="false">
      <defs>
        <linearGradient id="gradSite" x1="0" y1="0" x2="1" y2="1">
          <stop offset="0" stop-color="#e6e6e6"/>
          <stop offset="1" stop-color="#6d6d6d"/>
        </linearGradient>
      </defs>
      <polygon points="0,640 384,470 384,860 0,860" fill="url(#gradSite)" role="img" aria-label="Photo of an ironworker in a green hard hat on a steel construction site"/>
      <polygon points="160,860 384,690 384,760 250,860" fill="var(--gold)"/>
      <polygon points="0,620 384,455 384,472 0,642" fill="var(--navy)"/>
    </svg>
    <div class="skills">
      <h2 class="section-title">Skills/Traits:</h2>
      <div class="skill-columns">
        <ul class="skill-list">
          <li>Welding</li><li>bolting</li><li>rigging</li><li>connecting</li><li>Community service</li>
        </ul>
        <ul class="skill-list">
          <li>Teamwork</li><li>camaraderie</li><li>TK Grant</li><li>Skilled Labor</li><li>Career</li>
        </ul>
      </div>
    </div>
    <div class="career">
      <h2 class="section-title">OJT, Apprenticeship, Career:</h2>
      <p>Due to the large number of retirees from the baby boomer generation, ironworkers are in high demand. In Texas, the construction industry is on the rise and due to our training regiment, an average of 40 hrs/wk are worked. Our apprenticeship program follows the PLWTO curriculum and at the end of the 3-year course involving classroom learning, OJT and practical application the apprentice achieves journeymen status in ironworking. Journeyman status opens the door to possible postions like foremen, crane operators and project managers. Ironworkers perform their duties on steel structures that provide a skeleton for commercial buildings like hospitals, schools and skyscrapers. Some of the key skilled trades of ironworking are welding, rigging.</p>
    </div>
  </section>

  <!-- Back panel: logo and contact -->
  <section class="panel panel--back">
    <svg class="shapes" viewBox="0 0 384 860">
      <defs>
        <linearGradient id="gradWhite" x1="0" y1="0" x2="1" y2="1">
          <stop offset="0" stop-color="#ffffff"/>
          <stop offset="1" stop-color="#cfd3d8"/>
        </linearGradient>
      </defs>
      <polygon points="0,0 384,0 384,90 0,230" fill="url(#gradWhite)"/>
      <polygon points="0,0 60,0 384,190 384,240" fill="var(--gold)"/>
      <polygon points="60,0 384,0 384,190" fill="url(#gradWhite)"/>
    </svg>
    <div class="logo">
      <span class="logo__mark"><span class="logo__dot"></span>BDR</span>
      <span class="logo__name">BRAVO DIVISION REBUILD</span>
    </div>
    <div class="photo-frames">
      <div class="photo-frame" role="img" aria-label="Photo of an ironworker bolting a steel column"></div>
      <div class="photo-frame photo-frame--beam" role="img" aria-label="Photo of a steel beam lifted against the sky"></div>
    </div>
    <div class="contact">
      <p class="contact__phone">CALL US: (555) 014-2290</p>
      <p class="contact__email">EMAIL: Recruiting@BDRTexas.com</p>
      <p class="contact__web">www.bdrtexas.com</p>
    </div>
  </section>

  <!-- Cover panel -->
  <section class="panel panel--cover">
    <svg class="shapes" viewBox="0 0 384 860">
      <defs>
        <linearGradient id="gradSteel" x1="0" y1="0" x2="0" y2="1">
          <stop offset="0" stop-color="#e9eef4"/>
          <stop offset=".45" stop-color="var(--sky)"/>
          <stop offset="1" stop-color="var(--steel)"/>
        </linearGradient>
      </defs>
      <polygon points="0,0 384,0 384,330 200,610 0,450" fill="var(--gold)"/>
      <polygon points="0,0 384,0 384,300 200,580 0,430" fill="url(#gradSteel)" role="img" aria-label="Photo of ironworkers in harnesses on a steel frame under a blue sky"/>
    </svg>
    <div class="logo">
      <span class="logo__mark"><span class="logo__dot"></span>BDR</span>
      <span class="logo__name">BRAVO DIVISION REBUILD</span>
    </div>
    <div class="slogan">
      <p class="slogan__lead">Revolutionizing</p>
      <p class="slogan__main">The skilled workforce</p>
      <p class="slogan__tail">one Veteran at a time</p>
    </div>
    <div class="web-pill">www.bdrtexas.com</div>
  </section>

</main>
</body>
</html>
```